Health & Nutrition - Business Cards

Needs to look new-age, simple, and elegant. The cards are for my services/counsel in health and nutrition - which include mind, body, and soul. I would like to see something clean and simple but beautiful. Can have a plain background or with a pattern but I don't want it to take away from my contact details. Therefore, my info can be on the back of the card and a nice front design. I really like the flower of life symbol. The name of my business is called Velvet Meadow.

Target Market(s)

Clients - men & women age 20-60. Adults, parents, teachers, sick individuals seeking nutrient counseling and dietary management.

Industry/Entity Type

Nutritionist

Contact Information for Business Card

Tomas Brindle
Cell: 345-827-4602
Email: tbrindle@quillpost.example

Colors
33a6d7
33b8a4
add136
ffffff
5c5c5c
f04a50
fbee3f
cedeed
85cae6

Requirements
Nice to have
• Maybe it can have some sort of sacred geometry as well, but not required. Nice to have the colors that I choose in the project but feel free to come up with your own use of colors. Thanks! =)

```html
<!DOCTYPE html>
<html lang="en">
<head>
<meta charset="utf-8">
<title>Velvet Meadow – Business Cards</title>
<link rel="stylesheet" href="https://fonts.googleapis.com/css2?family=Cinzel:wght@400;500&family=Lato:wght@400&display=swap">
<style>
  :root {
    --backdrop: #212121;
    --card-light: #ffffff;
    --card-dark: #5c5c5c;
    --accent-red: #f04a50;
    --ink-grey: #5c5c5c;
    --ink-dark: #222222;
    --ink-white: #ffffff;
  }
  * { margin: 0; padding: 0; box-sizing: border-box; }
  html, body {
    width: 1200px;
    height: 900px;
    overflow: hidden;
    background: var(--backdrop);
  }
  .canvas {
    position: relative;
    width: 1200px;
    height: 900px;
  }
  .card {
    position: absolute;
    top: 200px;
    width: 310px;
    height: 502px;
  }
  .card--front {
    left: 253px;
    background: var(--card-light);
    border-radius: 58px 0 58px 0;
  }
  .card--back {
    left: 627px;
    background: var(--card-dark);
    border-radius: 0 58px 0 58px;
  }
  .brand-mark {
    position: absolute;
    left: 97px;
    top: 83px;
    width: 116px;
    height: 116px;
    border: 8px solid var(--accent-red);
    border-radius: 50%;
  }
  .brand-name {
    position: absolute;
    left: 0;
    width: 100%;
    top: 205px;
    text-align: center;
    font-family: "Cinzel", serif;
    font-weight: 400;
    font-size: 22px;
    letter-spacing: 0.5px;
    color: var(--accent-red);
  }
  .person-name {
    position: absolute;
    left: 33px;
    top: 328px;
    font-family: "Cinzel", serif;
    font-weight: 400;
    font-size: 27px;
    letter-spacing: 0.5px;
    color: var(--ink-grey);
  }
  .person-name .first { color: var(--accent-red); }
  .contact-list {
    position: absolute;
    left: 33px;
    top: 403px;
    list-style: none;
    font-family: "Lato", sans-serif;
    font-size: 17.5px;
    line-height: 23px;
    color: var(--ink-dark);
  }
  .contact-list li {
    display: flex;
    align-items: center;
    gap: 6px;
  }
  .contact-icon {
    width: 16px;
    height: 14px;
    flex: none;
  }
  .back-mark {
    position: absolute;
    left: 64px;
    top: 160px;
    width: 182px;
    height: 182px;
    border: 12px solid var(--accent-red);
    border-radius: 50%;
    display: flex;
    align-items: center;
    justify-content: center;
  }
  .back-name {
    font-family: "Cinzel", serif;
    font-weight: 400;
    font-size: 17px;
    line-height: 24px;
    text-align: center;
    color: var(--ink-white);
  }
</style>
</head>
<body>
<main class="canvas">
  <section class="card card--front">
    <div class="brand-mark" aria-hidden="true"></div>
    <p class="brand-name">Velvet Meadow</p>

    <h1 class="person-name"><span class="first">Tomas</span> Brindle</h1>

    <ul class="contact-list">
      <li>
        <svg class="contact-icon" viewBox="0 0 16 14" aria-hidden="true">
          <path fill="var(--accent-red)" d="M1 4.5C1 2.5 4 1 8 1s7 1.5 7 3.5v1.2h-3.2V4.3H4.2v1.4H1z"/>
          <path fill="var(--accent-red)" d="M4.5 6h7l2.5 4v3H2v-3z"/>
          <circle cx="8" cy="9.5" r="1.6" fill="#fff"/>
        </svg>
        345-827-4602
      </li>
      <li>
        <svg class="contact-icon" viewBox="0 0 16 14" aria-hidden="true">
          <rect x="0.5" y="2" width="15" height="11" fill="var(--accent-red)"/>
          <path d="M1 2.5l7 5.5 7-5.5M1 12.5l5-4.5M15 12.5l-5-4.5" fill="none" stroke="#fff" stroke-width="1"/>
        </svg>
        tbrindle@quillpost.example
      </li>
    </ul>
  </section>

  <section class="card card--back">
    <div class="back-mark">
      <p class="back-name">Velvet<br>Meadow</p>
    </div>
  </section>
</main>
</body>
</html>
```